Update our OBGYN business card look and info

We are an OBGYN office. Our logo is nice but would like to "woman" part of the logo to be a darker color, to contrast with the flower that surrounds it. Maybe make our practice name Harbor Bloom Care Clinic more feminine. Our practice caters to women only. All providers and staff are female.

Target Market(s)

Females 16-65.

Industry/Entity Type

Business

Contact Information for Business Card

See attached upload. The ONLY CHANGE to the information is DELETE the name Dorothy Kemplin, Midwife and REPLACE with Greta Poundsworth, Midwife

Logo Text

Harbor Bloom Care Clinic Obstetrics & Gynecology

Font styles to use
Serif
Script

Colors
85cae6
0692cd
33a6d7
85abd2
f59195
eea4c8
cadf82
fac994
d3a5cc

```html
<!DOCTYPE html>
<html lang="en">
<head>
<meta charset="utf-8">
<title>Harbor Bloom Care Clinic – Business Card</title>
<link href="https://fonts.googleapis.com/css2?family=Grand+Hotel&family=Jost:wght@400;500&display=swap" rel="stylesheet">
<style>
  :root {
    --bg: #2b2b2d;
    --sky: #85cae6;
    --sky-deep: #6fbcd9;
    --sky-light: #9dd6ec;
    --white: #ffffff;
    --grey: #8a8a8c;
    --grey-text: #6f6f72;
  }
  html, body {
    margin: 0;
    width: 1200px;
    height: 900px;
    overflow: hidden;
    background: var(--bg);
  }
  .canvas {
    position: relative;
    width: 1200px;
    height: 900px;
  }
  .card {
    position: absolute;
    left: 285px;
    width: 630px;
    height: 360px;
    border-radius: 22px;
    overflow: hidden;
  }
  .card--front {
    top: 60px;
    background: linear-gradient(135deg, var(--sky-deep) 0%, var(--sky) 55%, var(--sky-light) 100%);
  }
  .card--back {
    top: 480px;
    background: var(--white);
  }
  .wave {
    position: absolute;
    inset: 0;
    width: 630px;
    height: 360px;
  }
  .brand {
    position: absolute;
    display: flex;
    align-items: center;
    gap: 16px;
  }
  .brand__dot {
    width: 34px;
    height: 34px;
    border-radius: 50%;
    flex: none;
  }
  .brand__name {
    font-family: "Grand Hotel", cursive;
    font-size: 40px;
    line-height: 1;
    margin: 0;
    font-weight: 400;
  }
  .brand__tagline {
    font-family: "Jost", sans-serif;
    font-weight: 500;
    font-size: 17px;
    letter-spacing: 0.5px;
    margin: 6px 0 0 4px;
  }
  .card--front .brand { left: 70px; top: 140px; }
  .card--front .brand__dot { background: var(--white); }
  .card--front .brand__name,
  .card--front .brand__tagline { color: var(--white); }

  .card--back .brand { left: 30px; top: 26px; }
  .card--back .brand__name { font-size: 36px; color: var(--sky-deep); }
  .card--back .brand__tagline { font-size: 16px; color: var(--grey-text); }
  .card--back .brand__dot { background: var(--sky); }

  .providers {
    position: absolute;
    left: 40px;
    bottom: 22px;
    margin: 0;
    padding: 0;
    list-style: none;
    font-family: "Jost", sans-serif;
    font-size: 15px;
    line-height: 1.35;
    color: var(--white);
    letter-spacing: 0.3px;
  }
  .contact {
    position: absolute;
    right: 30px;
    top: 140px;
    font-family: "Jost", sans-serif;
    font-size: 15px;
    line-height: 1.35;
    color: var(--white);
    text-align: right;
    letter-spacing: 0.3px;
    display: flex;
    gap: 12px;
  }
  .contact__lines p { margin: 0; }
  .contact__lines .address { margin-bottom: 10px; }
  .contact__icons {
    display: flex;
    flex-direction: column;
    gap: 10px;
    padding-top: 2px;
  }
  .contact__icons svg { width: 14px; height: 14px; display: block; }
</style>
</head>
<body>
<main class="canvas">

  <section class="card card--front" aria-label="Card front">
    <div class="brand">
      <span class="brand__dot"></span>
      <div>
        <h1 class="brand__name">Harbor Bloom Care Clinic</h1>
        <p class="brand__tagline">Obstetrics &amp; Gynecology</p>
      </div>
    </div>
  </section>

  <section class="card card--back" aria-label="Card back">
    <svg class="wave" viewBox="0 0 630 360" aria-hidden="true">
      <path d="M0 204 C 150 202 240 194 310 140 S 490 42 630 34 L630 360 L0 360 Z" fill="var(--sky)"/>
      <path d="M0 198 C 150 196 240 188 308 134 S 490 36 630 28" fill="none" stroke="var(--grey)" stroke-width="6"/>
    </svg>

    <div class="brand">
      <span class="brand__dot"></span>
      <div>
        <h2 class="brand__name">Harbor Bloom Care Clinic</h2>
        <p class="brand__tagline">Obstetrics &amp; Gynecology</p>
      </div>
    </div>

    <ul class="providers">
      <li>Maren Ashcombe, MD</li>
      <li>Lydia Frenwick, MD</li>
      <li>Corinne Vasel, MD</li>
      <li>Greta Poundsworth, Midwife</li>
      <li>Nadia Trelling, Midwife</li>
    </ul>

    <div class="contact">
      <div class="contact__lines">
        <p>418 Lindell Ave, Ste 3B</p>
        <p class="address">Carverton, GA 31788 - 4402</p>
        <p>(555) 310-2847</p>
        <p>(555) 310-2915</p>
        <p>harborbloomcare.com</p>
      </div>
      <div class="contact__icons" aria-hidden="true">
        <svg viewBox="0 0 16 16"><path d="M3 1.5l3 .5 1 3.5-2 1.2a9 9 0 0 0 4.3 4.3l1.2-2 3.5 1 .5 3c-.3 1-1.2 1.5-2.2 1.5C6.5 14.5 1.5 9.5 1.5 3.7 1.5 2.7 2 1.8 3 1.5z" fill="var(--white)"/></svg>
        <svg viewBox="0 0 16 16"><path d="M2 15V5h5V1h7v14H2z" fill="var(--white)"/><rect x="9" y="3.5" width="2" height="2" fill="var(--sky)"/><rect x="9" y="7" width="2" height="2" fill="var(--sky)"/><rect x="4" y="8" width="2" height="2" fill="var(--sky)"/><rect x="7" y="11" width="2" height="4" fill="var(--sky)"/></svg>
        <svg viewBox="0 0 16 16"><circle cx="8" cy="8" r="6.5" fill="none" stroke="var(--white)" stroke-width="1.5"/><ellipse cx="8" cy="8" rx="2.8" ry="6.5" fill="none" stroke="var(--white)" stroke-width="1.2"/><path d="M1.5 8h13M2.5 5h11M2.5 11h11" stroke="var(--white)" stroke-width="1"/></svg>
      </div>
    </div>
  </section>

</main>
</body>
</html>
```